BrivoLane Ute.

I want the full logo on one side. And the other side the card if right Ralf the logo the left half orange like the car in the logo color with Danielle R Morrow
Founder and CEO
Email symbol then dmorrow@brivolaneute.com
Www symbol. Then Brivolaneute.com
Phone symbol then 413-926-BRIV
The very bottom would like Brivo Lane Ute is a division of Harmond Vistas. LLC

```html
<!DOCTYPE html>
<html lang="en">
<head>
<meta charset="utf-8">
<title>Brivo Lane Ute – Business Cards</title>
<link href="https://fonts.googleapis.com/css2?family=Work+Sans:wght@400;500;700&display=swap" rel="stylesheet">
<style>
  :root {
    --page-bg: #e9e9ec;
    --card-white: #ffffff;
    --orange-deep: #e7761c;
    --orange-light: #f29c30;
    --ink: #2b2b2b;
    --white: #ffffff;
  }
  * { box-sizing: border-box; margin: 0; padding: 0; }
  html, body { width: 1200px; height: 900px; overflow: hidden; }
  body {
    background: var(--page-bg);
    font-family: "Work Sans", Arial, sans-serif;
    display: flex;
    align-items: center;
    justify-content: center;
    gap: 40px;
  }
  .card {
    position: relative;
    width: 540px;
    height: 309px;
    background: var(--card-white);
    box-shadow: 0 6px 18px rgba(0,0,0,0.15);
    overflow: hidden;
  }

  /* Contact side */
  .card-contact .contact-panel {
    position: absolute;
    left: 0; top: 0;
    width: 270px; height: 100%;
    background: linear-gradient(135deg, var(--orange-deep), var(--orange-light));
    color: var(--white);
    padding: 34px 28px;
  }
  .person-name { font-size: 19px; font-weight: 700; letter-spacing: 0.2px; }
  .person-title { font-size: 10px; font-weight: 400; letter-spacing: 1px; margin-top: 4px; opacity: 0.9; }
  .contact-list { list-style: none; margin-top: 26px; }
  .contact-item {
    display: flex; align-items: center; gap: 10px;
    font-size: 11px; margin-bottom: 9px;
  }
  .contact-item svg { width: 12px; height: 12px; flex: none; }
  .panel-rule {
    position: absolute;
    left: 28px; top: 232px;
    width: 120px; height: 1px;
    background: var(--white);
    opacity: 0.85;
  }
  .card-contact .logo-area {
    position: absolute;
    left: 270px; top: 0;
    width: 270px; height: 230px;
    display: flex; align-items: center; justify-content: center;
  }
  .accent-rule {
    position: absolute;
    left: 290px; bottom: 60px;
    width: 220px; height: 2px;
    background: linear-gradient(90deg, var(--orange-deep), rgba(231,118,28,0.15));
  }
  .division-note {
    position: absolute;
    left: 290px; right: 20px; bottom: 28px;
    font-size: 11px; font-weight: 700;
    color: var(--ink);
    white-space: nowrap;
  }

  /* Brand name block */
  .brand-name {
    display: flex; align-items: center; gap: 10px;
    font-size: 26px; font-weight: 700;
    color: var(--ink);
    letter-spacing: 0.5px;
    white-space: nowrap;
  }
  .brand-dot {
    width: 18px; height: 18px; border-radius: 50%;
    background: var(--orange-deep);
  }

  /* Logo side */
  .card-logo .frame-outer {
    position: absolute; inset: 14px;
    border: 1.5px solid var(--orange-light);
  }
  .card-logo .frame-inner {
    position: absolute; inset: 19px;
    border: 1px solid var(--orange-light);
  }
  .card-logo .logo-area {
    position: absolute; inset: 0;
    display: flex; align-items: center; justify-content: center;
  }
  .card-logo .brand-name { font-size: 34px; }
  .card-logo .brand-dot { width: 22px; height: 22px; }
</style>
</head>
<body>

  <section class="card card-contact" aria-label="Contact side">
    <div class="contact-panel">
      <h1 class="person-name">Danielle R Morrow</h1>
      <p class="person-title">FOUNDER &amp; CEO</p>
      <ul class="contact-list">
        <li class="contact-item">
          <svg viewBox="0 0 12 12" aria-hidden="true"><circle cx="6" cy="6" r="5" fill="none" stroke="#fff" stroke-width="1.2"/><circle cx="6" cy="6" r="2" fill="none" stroke="#fff" stroke-width="1.2"/></svg>
          dmorrow@brivolaneute.com
        </li>
        <li class="contact-item">
          <svg viewBox="0 0 12 12" aria-hidden="true"><circle cx="6" cy="6" r="5" fill="none" stroke="#fff" stroke-width="1.1"/><ellipse cx="6" cy="6" rx="2.2" ry="5" fill="none" stroke="#fff" stroke-width="1"/><line x1="1" y1="6" x2="11" y2="6" stroke="#fff" stroke-width="1"/></svg>
          Brivolaneute.com
        </li>
        <li class="contact-item">
          <svg viewBox="0 0 12 12" aria-hidden="true"><path d="M3 1 L5 3.5 L4 5 Q5 7.5 7 8 L8.5 7 L11 9 L9.5 11 Q3.5 10.5 1 3 Z" fill="#fff"/></svg>
          413-926-BRIV
        </li>
      </ul>
      <div class="panel-rule"></div>
    </div>
    <div class="logo-area">
      <div class="brand-name"><span class="brand-dot"></span>Brivo Lane Ute</div>
    </div>
    <div class="accent-rule"></div>
    <p class="division-note">Harmond Vistas. LLC / Brivo Lane Ute</p>
  </section>

  <section class="card card-logo" aria-label="Logo side">
    <div class="frame-outer"></div>
    <div class="frame-inner"></div>
    <div class="logo-area">
      <div class="brand-name"><span class="brand-dot"></span>Brivo Lane Ute</div>
    </div>
  </section>

</body>
</html>
```